NEW! Sports Supplement label
Vital Kinetic Laboratories
Project: NEW! Sports Supplement label
NEW! Sports Supplement label - Sports
Creative Brief
Looking for a new packaging design for a new line of products. This needs to be a clean label that delivers a scientific or medical feel in 3 colors with 4 lines for product descriptor sublines. <p><p> For Example: <p> • Muscle Recovery Acceleration <p> • Nitric Oxide Production <p> • Maximum Muscle Mass <p> • Improved Energy &amp; Focus <p><p> Use the following elements for presentation: <p><p> Name: VK260Q <p><p> 120 Capsules Dietary Supplement <p><p> The products are geared to Sports Supplements, Fat burners, preworkout supplements, sport drinks. <p><p> The fonts for the Product name and VKL logo must be destinctive elements and pop that adds value by providing consumers with instantly recognizable cues to help with the purchase decision making process. Preferrably reversed out white or black. <p> <p> Please see the following sites as example product labels for creative thought. They also provide actual full labels for your review: <p><p> http://www.plorvex.com/product/index.jsp?productId=48573920 http://www.plorvex.com/product/index.jsp?productId=48619375 http://www.plorvex.com/product/index.jsp?productId=48926054 <p><p> The label should be clean, in that it provides a clear, attractive space, with key information (4 line product descriptor mentioned above) on the front display panel necessary for a consumer to make a quick purchase decision. <p> The label should communicate a concise but informative message designed to make the consumer feel comfortable with the product by providing consumers with instantly recognizable cues (symbols of quality) to help with the purchase decision making process.
Sports
Sports nutrition products target a mass audience of consumers who have grown up knowing an active lifestyle has positive, long-term implications for health, fitness, weight management and longevity.
Please provide label design with color codes and in standard file formats with element layers. 2.75 x 7.00 4 x 9.375

```html
<!DOCTYPE html>
<html lang="en">
<head>
<meta charset="utf-8">
<title>VK260Q Label Presentation</title>
<link rel="stylesheet" href="https://fonts.googleapis.com/css2?family=Russo+One&family=Roboto+Condensed:wght@400;700&display=swap">
<style>
  :root{
    --bg-top:#f4f4f4;
    --bg-bottom:#c9c9c9;
    --ink:#111111;
    --panel:#1a1a1a;
    --white:#ffffff;
    --red:#c8141b;
    --red-dark:#7d0b10;
    --blue:#1f2f8f;
    --blue-dark:#131c5c;
    --grey-text:#555555;
    --rule:#9a9a9a;
  }
  *{box-sizing:border-box;margin:0;padding:0}
  html,body{width:1200px;height:915px;overflow:hidden}
  body{
    position:relative;
    background:linear-gradient(180deg,var(--bg-top) 0%,#e2e2e2 60%,var(--bg-bottom) 100%);
    font-family:"Roboto Condensed",Arial,sans-serif;
    color:var(--ink);
  }

  /* ---------- label ---------- */
  .label{
    position:absolute;
    display:grid;
    grid-template-columns:30% 40% 30%;
    background:var(--white);
    box-shadow:0 4px 10px rgba(0,0,0,.25);
    --accent:var(--red);
    --accent-dark:var(--red-dark);
  }
  .label--big{--accent:var(--blue);--accent-dark:var(--blue-dark)}
  .label--small{left:50px;top:248px;width:500px;height:154px;font-size:5px}
  .label--big{left:595px;top:203px;width:590px;height:238px;font-size:7px}

  .label__back{padding:4% 5%;display:flex;flex-direction:column;gap:4%;background:var(--white)}
  .label__directions{background:var(--panel);color:var(--white);padding:4%;line-height:1.3}
  .dose-table{width:100%;border-collapse:collapse;font-size:1em}
  .dose-table th,.dose-table td{border:1px solid var(--rule);padding:1px 3px;text-align:left}
  .dose-table th{font-weight:700}
  .label__maker{color:var(--grey-text);margin-top:auto}

  .label__front{
    position:relative;display:flex;flex-direction:column;
    border-left:2px solid var(--accent);border-right:2px solid var(--accent);
  }
  .front__top{
    height:20%;background:var(--panel);
    border-bottom:4px solid var(--accent);
    display:flex;align-items:center;justify-content:center;
  }
  .brand{
    font-family:"Russo One",Arial,sans-serif;color:var(--white);
    font-size:2.6em;letter-spacing:.05em;display:flex;align-items:center;gap:.3em;
  }
  .brand__dot{width:.5em;height:.5em;background:var(--accent);display:inline-block}
  .front__title{
    height:30%;display:flex;flex-direction:column;align-items:center;justify-content:center;
    background:linear-gradient(180deg,#ffffff,#e9e9e9);
  }
  .product-name{font-family:"Russo One",Arial,sans-serif;font-size:6.4em;line-height:1;color:var(--ink);letter-spacing:.02em}
  .product-type{font-weight:700;font-size:1.5em;letter-spacing:.15em;margin-top:.2em}
  .front__claims{
    flex:1;background:linear-gradient(180deg,#3a3a3a,var(--panel));
    border-top:4px solid var(--accent);border-bottom:4px solid var(--accent);
    padding:4% 10%;color:var(--white);list-style:none;
    display:flex;flex-direction:column;justify-content:center;gap:6%;
  }
  .front__claims li{font-size:1.45em;display:flex;align-items:center;gap:.5em;
    background:rgba(255,255,255,.08);padding:.15em .4em}
  .front__claims li::before{content:"";width:.55em;height:.55em;background:var(--accent);flex:none}
  .front__count{
    position:absolute;left:0;bottom:0;background:var(--accent);color:var(--white);
    font-weight:700;font-size:1.4em;padding:.2em .6em;
  }
  .front__base{height:7%;background:var(--accent-dark)}

  .label__facts{padding:4% 5%;display:flex;flex-direction:column;gap:4%}
  .facts-box{border:1px solid var(--ink);padding:3% 4%}
  .facts-box h3{font-size:2em;font-weight:700;border-bottom:2px solid var(--ink);line-height:1.1}
  .facts-box p{border-bottom:1px solid var(--rule);padding:1px 0}
  .label__warning{color:var(--grey-text);line-height:1.3}

  .caption{
    position:absolute;top:478px;font-size:19px;color:#333;
    transform:translateX(-50%);white-space:nowrap;
  }
  .caption--small{left:298px}
  .caption--big{left:888px}

  .showcase-name{
    position:absolute;left:0;top:782px;width:520px;height:70px;
    background:linear-gradient(90deg,#2b2b2b,#6a6a6a 70%,rgba(106,106,106,0));
    display:flex;align-items:center;padding-left:37px;
  }
  .showcase-name span{font-family:"Russo One",Arial,sans-serif;font-size:60px;color:var(--white);letter-spacing:.04em}
</style>
</head>
<body>

  <section class="label label--small" aria-label="Small label, 2.75 by 7 inches">
    <div class="label__back">
      <p class="label__directions">Directions: Take two capsules daily with water before training. Do not exceed four capsules per day.</p>
      <table class="dose-table">
        <tr><th>OCCASION</th><th># OF CAPS</th></tr>
        <tr><td>Pre-workout</td><td>2</td></tr>
        <tr><td>Post-workout</td><td>2</td></tr>
        <tr><td>Rest day</td><td>1</td></tr>
      </table>
      <p class="label__maker">Manufactured for Vital Kinetic Laboratories</p>
    </div>
    <div class="label__front">
      <div class="front__top"><span class="brand"><i class="brand__dot"></i>VKL</span></div>
      <div class="front__title">
        <span class="product-name">VK260Q</span>
        <span class="product-type">DIETARY SUPPLEMENT</span>
      </div>
      <ul class="front__claims">
        <li>Muscle Recovery Acceleration</li>
        <li>Nitric Oxide Production</li>
        <li>Maximum Muscle Mass</li>
        <li>Improved Energy &amp; Focus</li>
      </ul>
      <span class="front__count">120</span>
      <div class="front__base"></div>
    </div>
    <div class="label__facts">
      <div class="facts-box">
        <h3>Supplement Facts</h3>
        <p>Serving Size 2 Capsules</p>
        <p>Servings Per Container 60</p>
      </div>
      <p class="label__warning">Warning: Consult a physician before use if pregnant or nursing.</p>
    </div>
  </section>

  <section class="label label--big" aria-label="Big label, 4 by 9.375 inches">
    <div class="label__back">
      <p class="label__directions">Directions: Take two capsules daily with water before training. Do not exceed four capsules per day.</p>
      <table class="dose-table">
        <tr><th>OCCASION</th><th># OF SCOOPS</th></tr>
        <tr><td>Pre-workout</td><td>2</td></tr>
        <tr><td>Post-workout</td><td>2</td></tr>
        <tr><td>Rest day</td><td>1</td></tr>
      </table>
      <p class="label__maker">Manufactured for Vital Kinetic Laboratories</p>
    </div>
    <div class="label__front">
      <div class="front__top"><span class="brand"><i class="brand__dot"></i>VKL</span></div>
      <div class="front__title">
        <span class="product-name">VK260Q</span>
        <span class="product-type">DIETARY SUPPLEMENT</span>
      </div>
      <ul class="front__claims">
        <li>Muscle Recovery Acceleration</li>
        <li>Nitric Oxide Production</li>
        <li>Maximum Muscle Mass</li>
        <li>Improved Energy &amp; Focus</li>
      </ul>
      <span class="front__count">120</span>
      <div class="front__base"></div>
    </div>
    <div class="label__facts">
      <div class="facts-box">
        <h3>Supplement Facts</h3>
        <p>Serving Size 2 Capsules</p>
        <p>Servings Per Container 60</p>
      </div>
      <p class="label__warning">Warning: Consult a physician before use if pregnant or nursing.</p>
    </div>
  </section>

  <p class="caption caption--small">2.75” X 7” (SMALL)</p>
  <p class="caption caption--big">4” X 9.375” (BIG)</p>

  <div class="showcase-name"><span>VK260Q</span></div>

</body>
</html>
```